DESIGN A LEAFLET FOR A CANNABIS CLUB!!

We need a leaflet design for a cannabis club based in the United Kingdom, called Silver Pond Cannabis Club

PLEASE, FEEL FREE TO ADD YOUR OWN INFO ETC

Just want attention drawn to the INSTAGRAM/WEBSITE whilst looking semi-professional

LEGALIZE IT (title)

Government officials are denying your right to access legal Cannabis.

Over Thirty-five countries already have legal access in one form or another... What are we waiting for ?

I'd ideally like the leaflet to be A6 size

"INSTAGRAM LOGO": Silverpondcannabisclub
*MUST SEE*
"FACEBOOK LOGO": Silverpondcannabisclub
WEB: www.silverpondcannabisclub-example.com

Check us out!
*Cannabis Discussion Forum*
*Weed related news*
*Awesome Documentaries*

Industry/Entity Type

Club

Requirements
Must have
• Please use my logo on leaflet somewhere, feel free to re-size it
• Back of leaflet to just have my cannabis logo in large with green and smoky background
Nice to have
• PLEASE, FEEL FREE TO ADD YOUR OWN INFO ETC
• Just want attention drawn to INSTAGRAM/WEBSITE whilst looking semi-professional
Should not have
• Plain, boring, minimal effort

```html
<!DOCTYPE html>
<html lang="en">
<head>
<meta charset="utf-8">
<title>Silver Pond Cannabis Club — Leaflet</title>
<link rel="stylesheet" href="https://fonts.googleapis.com/css2?family=Open+Sans:wght@400;600;700&display=swap">
<style>
  :root {
    --page-bg: #e4e2df;
    --forest-dark: #10231a;
    --forest-mid: #1f3a26;
    --forest-soft: #3b5a34;
    --panel-light: #f2f2f2;
    --text-grey: #5a5a5a;
    --icon-grey: #b4b4b4;
    --divider-brown: #8a5a3c;
    --club-green: #1e7a3a;
    --band-dark: #26302a;
    --glass-light: #a9aca4;
    --bud-green: #34432a;
    --bud-dark: #1f2a19;
    --shelf-brown: #8b5e3c;
    --white: #ffffff;
  }
  * { margin: 0; padding: 0; box-sizing: border-box; }
  html, body { width: 1200px; height: 882px; overflow: hidden; }
  body {
    background: var(--page-bg);
    font-family: "Open Sans", sans-serif;
    position: relative;
  }
  .leaflet {
    position: absolute;
    width: 491px;
    height: 692px;
    overflow: hidden;
    box-shadow: 0 6px 18px rgba(0,0,0,0.25);
  }
  .leaflet--front { left: 93px; top: 70px; background: var(--panel-light); }
  .leaflet--back {
    left: 641px; top: 136px; height: 694px;
    background: radial-gradient(ellipse at 45% 55%, var(--forest-soft) 0%, var(--forest-mid) 45%, var(--forest-dark) 100%);
  }

  /* Front: hero */
  .hero {
    position: absolute; left: 0; top: 0; width: 100%; height: 231px;
    background: radial-gradient(ellipse at 40% 85%, var(--forest-soft) 0%, var(--forest-mid) 45%, var(--forest-dark) 100%);
  }
  .brand {
    position: absolute; left: 0; right: 0;
    display: flex; flex-direction: column; align-items: center;
    color: var(--white); font-weight: 600; text-align: center;
  }
  .brand__dot { border-radius: 50%; background: var(--club-green); }
  .hero .brand { top: 34px; gap: 10px; font-size: 17px; }
  .hero .brand__dot { width: 40px; height: 40px; }
  .hero__title {
    position: absolute; left: 0; right: 0; top: 166px;
    text-align: center; color: var(--white);
    font-size: 35px; font-weight: 600; letter-spacing: 0.5px; line-height: 48px;
  }

  /* Front: two facts */
  .facts {
    position: absolute; left: 0; top: 231px; width: 100%; height: 197px;
    background: var(--panel-light);
    box-shadow: inset 0 6px 8px -6px rgba(0,0,0,0.35);
  }
  .facts__divider {
    position: absolute; left: 244px; top: 22px; width: 2px; height: 172px;
    background: var(--divider-brown);
  }
  .fact__text {
    position: absolute; top: 26px;
    text-align: center; color: var(--text-grey);
    font-size: 14.5px; line-height: 20px; white-space: nowrap;
  }
  .fact__text--left { left: 21px; width: 180px; }
  .fact__text--right { left: 266px; width: 200px; }
  .fact__icon { position: absolute; left: 73px; top: 99px; }
  .fact__map {
    position: absolute; left: 298px; top: 102px; width: 146px; height: 76px;
    background: linear-gradient(120deg, var(--icon-grey) 0%, var(--icon-grey) 68%, var(--club-green) 100%);
    border-radius: 6px;
  }

  .question-band {
    position: absolute; left: 0; top: 428px; width: 100%; height: 44px;
    background: var(--band-dark);
    color: var(--white); font-weight: 700; font-size: 17px;
    display: flex; align-items: center; justify-content: center; letter-spacing: 0.3px;
  }
  .product-photo {
    position: absolute; left: 0; top: 472px; width: 100%; height: 176px;
    background: linear-gradient(180deg,
      var(--glass-light) 0%, #7f857a 22%,
      var(--bud-green) 45%, var(--bud-dark) 70%,
      #4a3a2a 86%, var(--shelf-brown) 100%);
    border-top: 2px solid #c9ccc6;
  }

  .site-footer {
    position: absolute; left: 0; bottom: 0; width: 100%; height: 44px;
    background: var(--club-green);
    border-top: 3px solid var(--white);
    color: var(--white); font-size: 21px;
    display: flex; align-items: center; justify-content: center;
  }

  /* Back */
  .leaflet--back .brand { top: 230px; gap: 16px; font-size: 30px; line-height: 38px; }
  .leaflet--back .brand__dot { width: 70px; height: 70px; }
  .social {
    position: absolute; left: 0; right: 0; top: 524px;
    display: flex; justify-content: center; gap: 32px;
  }
  .social__dot { width: 32px; height: 32px; border-radius: 50%; background: var(--club-green); }
  .social__handle {
    position: absolute; left: 0; right: 0; top: 570px;
    text-align: center; color: var(--white); font-size: 15px;
  }
  .leaflet--back .site-footer { height: 46px; }
</style>
</head>
<body>

  <section class="leaflet leaflet--front">
    <header class="hero">
      <div class="brand">
        <span class="brand__dot"></span>
        <span class="brand__name">Silver Pond Cannabis Club</span>
      </div>
      <h1 class="hero__title">LEGALIZE IT!</h1>
    </header>

    <div class="facts">
      <p class="fact__text fact__text--left">Government officials are<br>denying your right to<br>access legal Cannabis.</p>
      <svg class="fact__icon" width="80" height="76" viewBox="0 0 100 95" aria-hidden="true">
        <polygon points="50,0 96,18 4,18" fill="var(--icon-grey)"/>
        <rect x="8" y="21" width="84" height="6" fill="var(--icon-grey)"/>
        <rect x="16" y="31" width="10" height="42" fill="var(--icon-grey)"/>
        <rect x="35" y="31" width="10" height="42" fill="var(--icon-grey)"/>
        <rect x="55" y="31" width="10" height="42" fill="var(--icon-grey)"/>
        <rect x="74" y="31" width="10" height="42" fill="var(--icon-grey)"/>
        <rect x="8" y="76" width="84" height="6" fill="var(--icon-grey)"/>
        <rect x="0" y="85" width="100" height="8" fill="var(--icon-grey)"/>
      </svg>
      <div class="facts__divider"></div>
      <p class="fact__text fact__text--right">Over Thirty-five countries<br>already have legal access<br>in one form or another...</p>
      <div class="fact__map" role="img" aria-label="Grey map of the United States with a green cannabis leaf"></div>
    </div>

    <div class="question-band">WHAT ARE WE WAITING FOR ?</div>
    <div class="product-photo" role="img" aria-label="Photo of glass jars filled with green cannabis buds lined up on a wooden shop shelf"></div>

    <footer class="site-footer">www.silverpondcannabisclub-example.com</footer>
  </section>

  <section class="leaflet leaflet--back" role="img" aria-label="Smoky green blurred cannabis plant background">
    <div class="brand">
      <span class="brand__dot"></span>
      <span class="brand__name">Silver Pond<br>Cannabis Club</span>
    </div>
    <div class="social">
      <span class="social__dot"></span>
      <span class="social__dot"></span>
    </div>
    <p class="social__handle">silverpondcannabisclub</p>
    <footer class="site-footer">www.silverpondcannabisclub-example.com</footer>
  </section>

</body>
</html>
```